Haventrix Corporate Stationery

Look for design of all new corporate stationery for an existing insurance broking business that is going through a redesign and move from older partners to younger family members. New Logo is attached. Company is Brisbane based.
Colours in the Logo is Hex #43bed8 and website features a lot of hex #17b8d8. Website front page "A plan to protect you" - headline. "Professional and Individual advice to protect your greatest assets" - tagline.

Stationery required: Business Cards, Letter head, Thank-you cards, Birthday cards, Presentation folders, With Compliment slips and a powerpoint template. We also would like to send a card to all customers with the something along of the lines of "something new".

Target Market(s)

Customers of Insurance business looking at superannuation, life and income protection insurance, investment advice and wills

Industry/Entity Type

Insurance Broker

Font styles to use
Other font styles liked:
• same as logo

Requirements
Must have
• The above designs for new stationery for the new business including:
• Business Cards, Letter head, Thank-you cards, Birthday cards, Presentation folders, With Compliment slips and a powerpoint template. We also would like to send a card to all customers with the something along of the lines of "something new".
Nice to have
• It is a new look - long time family business being passed to next generation - big focus on advice for YOU, individual advice etc..

```html
<!DOCTYPE html>
<html lang="en">
<head>
<meta charset="utf-8">
<title>Haventrix – New Look Announcement Card</title>
<link rel="stylesheet" href="https://fonts.googleapis.com/css2?family=Maven+Pro:wght@400;500;600&display=swap">
<style>
  :root {
    --page: #ffffff;
    --card: #ffffff;
    --ink: #7f7f82;
    --brand: #43bed8;
    --band: #dbf0f6;
    --floor: #f4f4f4;
  }
  * { margin: 0; padding: 0; box-sizing: border-box; }
  html, body {
    width: 1200px; height: 1000px; overflow: hidden;
    background: var(--page);
    font-family: "Maven Pro", sans-serif;
    color: var(--ink);
  }
  .announcement-card {
    position: absolute; left: 263px; top: 0;
    width: 673px; height: 1000px;
    background: var(--card);
    box-shadow: 0 0 8px rgba(0,0,0,0.12);
    overflow: hidden;
  }
  .growth-artwork {
    position: absolute; left: 0; top: 510px;
    width: 673px; height: 490px;
    clip-path: polygon(0 175px, 100% 0, 100% 100%, 0 100%);
    background: linear-gradient(172deg, var(--band) 0%, var(--band) 30%, var(--floor) 55%, var(--floor) 100%);
  }
  .headline {
    position: absolute; top: 116px; width: 100%;
    text-align: center; font-size: 48px; font-weight: 400;
    letter-spacing: 1.5px;
  }
  .brand {
    position: absolute; top: 262px; width: 100%;
    display: flex; flex-direction: column; align-items: center; gap: 26px;
  }
  .brand-dot { width: 110px; height: 110px; border-radius: 50%; background: var(--brand); }
  .brand-name {
    font-size: 62px; font-weight: 500; color: var(--brand);
    letter-spacing: 3px; line-height: 1;
  }
  .legacy {
    position: absolute; top: 674px; width: 100%;
    text-align: center; font-size: 30px; line-height: 41px; letter-spacing: 1.5px;
  }
  .promise {
    position: absolute; top: 791px; width: 100%;
    text-align: center; font-size: 25px; line-height: 34px; letter-spacing: 1.5px;
  }
</style>
</head>
<body>
  <main class="announcement-card">
    <div class="growth-artwork" role="img" aria-label="Rising growth arrow illustration in light blue and grey"></div>

    <h1 class="headline">We’ve got a new look.</h1>

    <div class="brand">
      <span class="brand-dot"></span>
      <span class="brand-name">Haventrix</span>
    </div>

    <p class="legacy">Haventrix has been passed on<br>from one generation to another</p>

    <p class="promise">Our main focus still remains the same:<br>We aim to provide you with the best<br>professional and individual advice to<br>protect your greatest assets</p>
  </main>
</body>
</html>
```